Automotive Accessories Business Card

Design a business template that match our new logo design and our industry.

https://www.kelvramotive.com/

Target Market(s)

Aftermarket auto parts and accessories

Industry/Entity Type

automotive

Contact Information for Business Card

company logo

Font styles to use
Serif
Sans Serif

Colors
EB3D1F
EC4F4E
F09395
F8D3D4
FCEDEE

```html
<!DOCTYPE html>
<html lang="en">
<head>
<meta charset="utf-8">
<title>Kelvra Motive – Business Card</title>
<link rel="stylesheet" href="https://fonts.googleapis.com/css2?family=Poppins:wght@400;500;600;700&display=swap">
<style>
  :root {
    --red: #e0232b;
    --charcoal: #3c3c3e;
    --ink: #2d2d2f;
    --paper: #ffffff;
    --carbon-dark: #0d0d0e;
    --carbon-mid: #232325;
    --stage: #ece9e4;
  }
  * { margin: 0; padding: 0; box-sizing: border-box; }
  html, body { width: 900px; height: 1200px; overflow: hidden; }
  body {
    position: relative;
    background: var(--stage);
    font-family: "Poppins", sans-serif;
    color: var(--ink);
  }
  .card {
    position: absolute;
    left: 80px;
    width: 735px;
    height: 428px;
    border-radius: 24px;
    overflow: hidden;
  }
  .card--front { top: 130px; background: var(--paper); }
  .card--back { top: 647px; }

  .wordmark {
    position: absolute;
    font-weight: 700;
    letter-spacing: 0.5px;
    line-height: 1;
    white-space: nowrap;
  }
  .card--front .wordmark { left: 36px; top: 74px; font-size: 37px; color: var(--red); }
  .card--back .wordmark { left: 0; right: 0; top: 175px; text-align: center; font-size: 56px; color: var(--paper); }

  .race-band { position: absolute; }
  .race-band--front { left: 400px; top: 68px; width: 335px; height: 50px; background: linear-gradient(180deg, var(--charcoal) 0 50%, var(--red) 50% 100%); }
  .race-band--back-left { left: 0; top: 387px; width: 180px; height: 22px; background: linear-gradient(180deg, var(--paper) 0 50%, var(--red) 50% 100%); }
  .race-band--back-right { right: 0; top: 387px; width: 178px; height: 22px; background: linear-gradient(180deg, var(--paper) 0 50%, var(--red) 50% 100%); }

  .rule { position: absolute; top: 222px; height: 3px; }
  .rule--red { left: 35px; width: 457px; background: var(--red); }
  .rule--dark { left: 500px; width: 204px; background: var(--charcoal); }

  .office { position: absolute; top: 245px; font-size: 16.5px; line-height: 23.5px; font-style: normal; color: var(--ink); }
  .office--us { left: 35px; }
  .office--ca { left: 500px; }
  .phone { display: flex; align-items: center; gap: 12px; margin-top: 9px; font-size: 19px; font-weight: 600; }
  .phone svg { width: 30px; height: 20px; }

  .email-band { position: absolute; left: 368px; top: 360px; width: 367px; height: 28px; }
  .email-band span { position: absolute; left: 75px; top: 1px; font-size: 17px; color: var(--paper); }
  .web-band { position: absolute; left: 0; top: 390px; width: 370px; height: 28px; }
  .web-band span { position: absolute; left: 94px; top: 2px; font-size: 16px; font-weight: 500; letter-spacing: 0.5px; color: var(--paper); }

  .carbon {
    position: absolute; inset: 0;
    background: radial-gradient(ellipse at 50% 40%, var(--carbon-mid), var(--carbon-dark) 75%);
  }
  .back-url {
    position: absolute; left: 0; right: 0; top: 385px;
    text-align: center; font-size: 18px; font-weight: 600; letter-spacing: 1px; color: var(--red);
  }
</style>
</head>
<body>

<section class="card card--front">
  <div class="wordmark">KELVRA MOTIVE</div>
  <div class="race-band race-band--front" role="img" aria-label="Checkered racing flag strip"></div>

  <div class="rule rule--red"></div>
  <div class="rule rule--dark"></div>

  <address class="office office--us">
    240 W. Harbor Ave. Unit C<br>Fairlane, CA, 91850<br>United States
    <div class="phone">
      <svg viewBox="0 0 30 20"><polygon points="5,0 30,0 25,20 0,20" fill="var(--red)"/><path d="M11 5c1 4 4 8 8 9l2-2-3-2-1 1c-2-1-3-3-4-4l1-1-1-3z" fill="#fff"/></svg>
      1-866-555-0142
    </div>
  </address>

  <address class="office office--ca">
    5120 Alder Crest St.<br>Vancouver, BC V5X 2K7<br>Canada
    <div class="phone">
      <svg viewBox="0 0 30 20"><polygon points="5,0 30,0 25,20 0,20" fill="var(--red)"/><path d="M11 5c1 4 4 8 8 9l2-2-3-2-1 1c-2-1-3-3-4-4l1-1-1-3z" fill="#fff"/></svg>
      604-555-0187
    </div>
  </address>

  <div class="email-band">
    <svg width="367" height="28" viewBox="0 0 367 28">
      <polygon points="62,0 367,0 367,28 52,28" fill="var(--charcoal)"/>
      <polygon points="14,0 62,0 52,28 0,28" fill="var(--red)"/>
      <rect x="21" y="8" width="17" height="12" fill="none" stroke="#fff" stroke-width="1.6"/>
      <polyline points="21,8 29.5,15 38,8" fill="none" stroke="#fff" stroke-width="1.6"/>
    </svg>
    <span>sales@kelvramotive.com</span>
  </div>

  <div class="web-band">
    <svg width="370" height="28" viewBox="0 0 370 28">
      <polygon points="0,0 82,0 72,28 0,28" fill="var(--charcoal)"/>
      <polygon points="82,0 370,0 355,28 66,28" fill="var(--red)"/>
      <circle cx="47" cy="14" r="8" fill="none" stroke="#fff" stroke-width="1.5"/>
      <ellipse cx="47" cy="14" rx="3.5" ry="8" fill="none" stroke="#fff" stroke-width="1.3"/>
      <line x1="39" y1="14" x2="55" y2="14" stroke="#fff" stroke-width="1.3"/>
    </svg>
    <span>WWW.KELVRAMOTIVE.COM</span>
  </div>
</section>

<section class="card card--back">
  <div class="carbon" role="img" aria-label="Black carbon fibre weave texture"></div>
  <div class="wordmark">KELVRA MOTIVE</div>
  <div class="race-band race-band--back-left" role="img" aria-label="Checkered racing flag strip"></div>
  <div class="back-url">WWW.KELVRAMOTIVE.COM</div>
  <div class="race-band race-band--back-right" role="img" aria-label="Checkered racing flag strip"></div>
</section>

</body>
</html>
```